Luxury Brand Vision Deck (Canva) | Coffee Table Book Style

I am looking for a designer to create a luxury, editorial-style pitch deck for a high-end hospitality brand (restaurants + lifestyle).

This deck must feel like a coffee table book, not a corporate presentation.

Non-Negotiable Requirements:
Must be designed in Canva
Clean, minimal, luxury aesthetic
Editorial / fashion-magazine inspired
Spacious layouts, strong typography
Designed to be reused as a template

Visual Style:
Black, white, cream, charcoal, soft neutrals
No bright colors
No gradients
No busy backgrounds
Elegant, modern fonts
Image-forward pages

Use Case:
Digital pitch deck
Later printed as a physical coffee table booklet
Reused for future meetings and brand presentations

I Will Provide:
All written content (slide-by-slide)
Brand context and inspiration
Image direction or assets

You Are a Good Fit If:
You love minimal, luxury design
You understand editorial layout and spacing
You have strong attention to detail
You enjoy premium branding projects
This project is about restraint, confidence, and elevated simplicity.

https://www.linkedin.com/company/lumo-by-the-bay/

https://www.lumobythebay.example/

Target Market(s)

Luxury hospitality / restaurant group leadership (owners, founders, executives)

Industry/Entity Type

Hospitality, Restaurants, Luxury Lifestyle Brand

Requirements
Must have
• Must be designed in Canva

```html
<!DOCTYPE html>
<html lang="en">
<head>
<meta charset="utf-8">
<title>Lumo Group — A Marketing Vision</title>
<link rel="stylesheet" href="https://fonts.googleapis.com/css2?family=Cinzel:wght@400;700&family=Marcellus&family=Lato:wght@400&display=swap">
<style>
  :root {
    --page: #ffffff;
    --cream: #f6f5f1;
    --ink: #2b2a28;
    --body: #6d6b67;
    --muted: #8c8a85;
    --photo-warm-top: #cfc6bb;
    --photo-warm-bottom: #b3a697;
    --photo-dusk-top: #a99a8c;
    --photo-dusk-bottom: #8e8690;
  }
  * { margin: 0; padding: 0; box-sizing: border-box; }
  html, body { width: 1200px; height: 1200px; overflow: hidden; background: var(--page); }
  .board { position: relative; width: 1200px; height: 1200px; }
  .slide { position: absolute; width: 481px; height: 271px; background: var(--cream); overflow: hidden; }
  .s1 { left: 98px; top: 121px; }
  .s2 { left: 631px; top: 121px; width: 480px; }
  .s3 { left: 96px; top: 468px; width: 480px; }
  .s4 { left: 630px; top: 468px; width: 480px; }
  .s5 { left: 96px; top: 815px; width: 483px; }
  .s6 { left: 631px; top: 815px; width: 483px; }

  .abs { position: absolute; }
  .heading {
    font-family: "Cinzel", serif; font-weight: 700; color: var(--ink);
    font-size: 11.5px; letter-spacing: 1.5px; line-height: 12.6px; text-transform: uppercase;
  }
  .copy { font-family: "Lato", sans-serif; color: var(--body); font-size: 5.4px; letter-spacing: 0.15px; line-height: 8.6px; }
  .copy p + p, .copy p + ul, .copy ul + p { margin-top: 8.6px; }
  .copy ul { list-style: none; padding-left: 4px; }
  .copy li::before { content: "•"; margin-right: 4px; }

  /* Cover */
  .cover-title {
    left: 0; right: 0; top: 222px; text-align: center;
    font-family: "Cinzel", serif; font-weight: 400; font-size: 29px; letter-spacing: 3.4px; line-height: 1; color: var(--ink);
  }
  .s1 .cover-title { top: 101px; }
  .cover-sub {
    left: 0; right: 0; top: 130px; text-align: center;
    font-family: "Marcellus", serif; font-size: 17px; letter-spacing: 3.6px; line-height: 1; color: var(--ink);
  }
  .cover-lede {
    left: 130px; width: 222px; top: 154px; text-align: center;
    font-family: "Lato", sans-serif; font-size: 4.6px; letter-spacing: 2.5px; line-height: 6.3px; color: var(--muted); text-transform: uppercase;
  }
  .cover-name {
    left: 0; right: 0; top: 244px; text-align: center;
    font-family: "Lato", sans-serif; font-size: 4.4px; letter-spacing: 1.6px; line-height: 4.8px; color: var(--muted);
  }

  .photo { position: absolute; left: 0; top: 0; width: 132px; height: 100%; }
  .photo-terrace { background: linear-gradient(180deg, var(--photo-warm-top), var(--photo-warm-bottom)); }
  .photo-lanterns { background: linear-gradient(180deg, var(--photo-dusk-top), var(--photo-dusk-bottom)); }

  .rating { left: 297px; font-family: "Cinzel", serif; color: var(--ink); display: flex; align-items: center; }
  .rating .stars { font-size: 17px; letter-spacing: 3px; line-height: 1; }
  .rating .score { font-size: 10px; font-weight: 700; letter-spacing: 1.2px; margin-left: 2px; }
</style>
</head>
<body>
<main class="board">

  <section class="slide s1">
    <h1 class="abs cover-title">LUMO GROUP</h1>
    <p class="abs cover-sub">A Marketing Vision</p>
    <p class="abs cover-lede">How I see the brand, where I believe it can go, and how I would help take it there.</p>
    <p class="abs cover-name">Elena Marsh<br>Director of Marketing Candidate</p>
  </section>

  <section class="slide s2">
    <div class="photo photo-terrace" role="img" aria-label="Photograph of a waterfront restaurant terrace"></div>
    <h2 class="abs heading" style="left:178px; top:55px;">Why Lumo is different</h2>
    <div class="abs copy" style="left:178px; top:81px; width:216px;">
      <p>Lumo Group isn't just a collection of restaurants. It's an energy. A mood. A place people want to be part of.</p>
      <p>Over the past year and a half, I've been deeply immersed in the Lumo ecosystem as a client, a collaborator, and a genuine fan of the brand. I've seen firsthand what makes these concepts special: the atmosphere, the people, the confidence, and the way guests feel both when they walk in and when they leave.</p>
      <p>What excites me most is that Lumo already has the hard part. The energy is real, and people feel it the moment they step into the space.</p>
      <p>The opportunity now is about refining and protecting that magic as the brand continues to grow. Making sure what guests experience in the room, what they see online, and what they hear about Lumo all tell the same elevated story, wherever they encounter the brand.</p>
    </div>
  </section>

  <section class="slide s3">
    <h2 class="abs heading" style="left:26px; top:72px;">Three pillars<br>I comeback to<br>every time</h2>
    <div class="abs copy" style="left:26px; top:124px; width:214px;">
      <p>When I think about taking a hospitality brand to the next level, I always return to three things:</p>
      <ul>
        <li>Reputation that reflects reality</li>
        <li>Identity that lives beyond the walls</li>
        <li>Details that quietly elevate everything</li>
      </ul>
      <p>These pillars guide how I prioritize, what I push forward first, and how I think about long-term brand equity rather than short-term noise.</p>
    </div>
  </section>

  <section class="slide s4">
    <div class="photo photo-lanterns" role="img" aria-label="Photograph of a celebration under woven lanterns"></div>
    <h2 class="abs heading" style="left:171px; top:60px;">A brand ready<br>for its next era</h2>
    <div class="abs copy" style="left:171px; top:102px; width:282px;">
      <p>Lumo already has what most brands spend years trying to manufacture. Energy. Identity. A loyal following. Cultural relevance.</p>
      <p>The restaurants are known. The rooms are full. The brand is respected. And this is often the exact moment where hospitality groups either plateau as an "it" spot or intentionally evolve into something bigger.</p>
      <p>The next chapter is not about awareness. It's about elevation.</p>
      <p>Elevation looks like tighter alignment between what people hear, what they see online, and what they experience in person. It looks like consistency across concepts without losing individuality. It looks like turning momentum into something scalable and durable.</p>
      <p>This is the stage Lumo is in now. And this is the work I'm genuinely excited to do.</p>
    </div>
  </section>

  <section class="slide s5">
    <h2 class="abs heading" style="left:27px; top:74px;">Priority one:<br>reviews &amp; reputation</h2>
    <div class="abs copy" style="left:27px; top:113px; width:220px;">
      <p>Searchly is often the final decision point. Even when someone hears about a restaurant through friends, social media, or word of mouth.</p>
      <p>A guest can be already excited to go, then do a quick search, see a 3.8 rating, and quietly choose a different restaurant. That friction is real, and it happens every day, especially in a market like Miami where guests have endless options.</p>
      <p>Lumo, Solenne, and Marivelle are high-quality, high-demand concepts. The current ratings don't reflect that reality. Which means the online reputation is likely costing the group first-time visits without anyone inside the business fully seeing the loss.</p>
    </div>
    <div class="abs rating" style="top:108px;"><span class="stars">★★★★☆</span><span class="score">3.8</span></div>
    <svg class="abs" style="left:297px; top:132px;" width="116" height="8" viewBox="0 0 116 8" aria-hidden="true">
      <line x1="0" y1="4" x2="112" y2="4" stroke="#2b2a28" stroke-width="1"/>
      <path d="M109 2 L113 4 L109 6" fill="none" stroke="#2b2a28" stroke-width="0.8"/>
    </svg>
    <div class="abs rating" style="top:145px;"><span class="stars">★★★★★</span><span class="score">4.5+</span></div>
  </section>

  <section class="slide s6">
    <h2 class="abs heading" style="left:27px; top:61px;">How I'd lift ratings<br>authentically</h2>
    <div class="abs copy" style="left:27px; top:100px; width:214px;">
      <p>Improving reviews isn't about asking harder. It's about building a system that makes it easy for happy guests to speak up.</p>
      <p>My approach would focus on:</p>
      <ul>
        <li>Natural, staff-aligned prompts that feel guest-first</li>
        <li>Post-visit follow-ups designed to capture satisfied diners</li>
        <li>Thoughtful incentives that feel elevated and on-brand</li>
        <li>Tracking progress monthly and treating reviews as a true brand health metric</li>
        <li>A simple internal rhythm: monitor, respond, refine, repeat</li>
      </ul>
      <p>The goal is not just a higher number. It's alignment between the real-life experience and what the world sees online.</p>
    </div>
  </section>

</main>
</body>
</html>
```